Web Design Project for lawn care business

after having a logo designed now my website is letting me down.
My websites main purpose is once i have made contact with a customer most will then try to research my company and the work i have done. Going to my unprofessional and untidy site will only put off potential customers. Also some customers will find my site online so must be able to grab their attention.

My site must be in keeping with my logo. Which is modern, sleek and classy. It needs to convey how professional we are and that the customer is getting a professional service.

My existing site will be replaced with the winning design.

Content wise and amount of pages will be similar to mine how ever more data will be inputted by myself.

so far prefer sites designed incorporating links in pictures or animated links to flick through pictures etc

breaks up the site and is more user friendly. 

also need to make sure colours are in keeping with logo or at least have similarities to keep it all uniform.

thanks

Industry/Entity Type

Lawn Care

Requirements
Nice to have
• in keeping font wise with my logo
same colours etc

```html
<!DOCTYPE html>
<html lang="en">
<head>
<meta charset="utf-8">
<title>Fairway Lawn Care</title>
<link rel="stylesheet" href="https://fonts.googleapis.com/css2?family=Cinzel:wght@400;700&family=Lato:wght@400;700&display=swap">
<style>
:root{
  --green:#6f9a1c;
  --green-dark:#4f7e17;
  --green-bright:#8dc21f;
  --ink:#222;
  --grey-text:#666;
  --bar:#333;
  --black:#000;
  --band:#ebebeb;
  --white:#fff;
}
*{margin:0;padding:0;box-sizing:border-box}
html,body{width:972px;height:1200px;overflow:hidden;background:var(--white)}
body{position:relative;font-family:"Lato",sans-serif;color:var(--ink)}
.abs{position:absolute}
.topbar{left:0;top:0;width:972px;height:33px;background:var(--bar)}
.search{left:107px;top:7px;width:199px;height:20px;background:var(--white);border:1px solid #ccc;font-size:7px;color:#aaa;padding:5px 6px}
.search svg{position:absolute;right:5px;top:4px}
.contact{top:8px;font-size:14px;line-height:16px}
.phone-num{left:604px;color:var(--green-bright)}
.email{left:734px;color:var(--white);font-size:13px}
.header{left:0;top:33px;width:972px;height:122px;background:var(--black)}
.brand{left:117px;top:78px;display:flex;align-items:center;gap:8px;font-family:"Cinzel",serif;font-size:20px;color:var(--green-bright)}
.brand-dot{width:30px;height:30px;border-radius:50%;background:var(--green-bright)}
.nav{top:87px;left:0;width:972px;font-size:14.5px;color:var(--white)}
.nav a{position:absolute;color:inherit;text-decoration:none;white-space:nowrap}
.nav a.active{color:var(--green-bright)}
.band{left:0;top:155px;width:972px;height:313px;background:var(--band)}
.hero{left:97px;top:165px;width:779px;height:326px;background:linear-gradient(#5d9be0 0%,#cfe4f6 45%,#7fbf3a 62%,#3f8f1a 100%)}
.hero-title{left:97px;top:286px;width:779px;text-align:center;padding-left:50px;font-family:"Cinzel",serif;font-size:24px;color:var(--green)}
.dots{left:803px;top:459px;display:flex;gap:4px}
.dots span{width:10px;height:10px;background:var(--green-bright)}
.dots span.on{background:var(--white)}
.card-img{top:514px;width:178px;height:96px}
.card-tag{top:572px;height:26px;background:rgba(90,140,30,.9);color:var(--white);font-family:"Cinzel",serif;font-size:10px;line-height:26px;padding:0 10px 0 16px}
.service{top:620px}
.service h3{font-family:"Cinzel",serif;font-weight:400;font-size:12.5px;color:var(--green);display:flex;align-items:center;gap:5px;margin-left:-10px}
.service ul{list-style:none;margin-top:6px;font-size:8.5px;line-height:14.6px;color:var(--grey-text)}
.about-band{left:97px;top:778px;width:779px;height:40px;background:linear-gradient(#f2f2f2,var(--white))}
.sec-title{top:796px;font-family:"Cinzel",serif;font-size:15px;color:var(--green)}
.subtitle{left:106px;top:819px;font-size:10px;color:#333}
.about-img{left:105px;top:849px;width:243px;height:135px;background:linear-gradient(#a9b48a,#6f9a3a 60%,#8aa84a)}
.about-text{left:365px;top:845px;width:242px;font-size:8.5px;line-height:14.6px;color:#444;text-align:justify}
.quote-img{left:624px;top:845px;width:48px;height:47px;background:linear-gradient(#c79a86,#b5322f)}
.quote{left:688px;top:849px;width:177px;font-size:8.5px;line-height:14.6px;color:#444;text-align:justify}
.quote b{font-family:Georgia,serif;font-size:16px;color:#333;line-height:8px}
.signup{left:104px;top:1017px;width:761px;height:73px;background:var(--bar)}
.signup h2{position:absolute;left:22px;top:26px;font-size:16px;font-weight:700;color:var(--white)}
.signup .field{position:absolute;left:313px;top:22px;width:323px;height:33px;background:var(--white);font-size:8px;color:#888;padding:12px 10px}
.signup .submit{position:absolute;left:652px;top:24px;width:83px;height:29px;background:linear-gradient(#7ab32a,var(--green-dark));color:var(--white);font-size:11px;text-align:center;line-height:29px}
.footer{left:0;top:1118px;width:972px;height:82px;background:var(--band)}
.foot-links{right:105px;top:1136px;font-size:10px;color:#555;word-spacing:2px}
.foot-links span{margin:0 7px;color:#777}
.copy{right:105px;top:1163px;font-size:9.5px;color:#555}
.social{left:105px;top:1147px;display:flex;gap:3px}
.social span{width:26px;height:26px;border-radius:50%}
</style>
</head>
<body>
<div class="abs topbar"></div>
<div class="abs search">Type search
  <svg width="10" height="10" viewBox="0 0 10 10"><circle cx="4" cy="4" r="3" fill="none" stroke="#999"/><line x1="6" y1="6" x2="9" y2="9" stroke="#999"/></svg>
</div>
<svg class="abs" style="left:565px;top:8px" width="14" height="18" viewBox="0 0 14 18"><path d="M3 1 L6 5 L4 7 Q6 11 9 13 L11 11 L14 14 L11 17 Q2 13 0 4 Z" fill="#ddd"/></svg>
<div class="abs contact phone-num">01632 960 418</div>
<svg class="abs" style="left:707px;top:10px" width="19" height="13" viewBox="0 0 19 13"><rect x=".5" y=".5" width="18" height="12" fill="none" stroke="#fff"/><path d="M.5 .5 L9.5 7 L18.5 .5" fill="none" stroke="#fff"/></svg>
<div class="abs contact email">hello@fairwaycare.net</div>

<header class="abs header"></header>
<div class="abs brand"><span class="brand-dot"></span>Fairway Lawn Care</div>
<nav class="abs nav">
  <a class="active" style="left:367px">Home</a>
  <a style="left:419px">Contact Us</a>
  <a style="left:505px">Our Services</a>
  <a style="left:606px">Useful Links</a>
  <a style="left:698px">Lawncare&nbsp; Advice</a>
  <a style="left:829px">FAQS</a>
</nav>

<div class="abs band"></div>
<div class="abs hero" role="img" aria-label="Sunny sky with clouds over a wide green lawn and a lone tree"></div>
<div class="abs hero-title">Fairway Lawn Care</div>
<div class="abs dots"><span></span><span></span><span></span><span class="on"></span></div>

<div class="abs card-img" style="left:105px;background:linear-gradient(#6ab22e,#3c86d6)" role="img" aria-label="Tree canopy against blue sky"></div>
<div class="abs card-tag" style="left:105px">Tree Services</div>
<div class="abs card-img" style="left:300px;background:linear-gradient(#4f7d2a,#86a63a 55%,#d0622a)" role="img" aria-label="Garden with tulip beds"></div>
<div class="abs card-tag" style="left:300px">Garden Services</div>
<div class="abs card-img" style="left:494px;background:linear-gradient(#9cc2e8,#c7b08f 50%,#5f9a30)" role="img" aria-label="House with front lawn"></div>
<div class="abs card-tag" style="left:494px">Lawn Services</div>
<div class="abs card-img" style="left:689px;background:linear-gradient(#6fae2c,#4a8a1c)" role="img" aria-label="Sports pitch corner with flag"></div>
<div class="abs card-tag" style="left:689px">Sports Surface Services</div>

<div class="abs service" style="left:122px">
  <h3><svg width="6" height="9"><path d="M1 1 L5 4.5 L1 8" fill="none" stroke="#555"/></svg>Tree Services</h3>
  <ul><li>Tree pruning</li><li>Tree shaping</li><li>Tree felling</li><li>Tree stump removal</li></ul>
</div>
<div class="abs service" style="left:322px">
  <h3><svg width="6" height="9"><path d="M1 1 L5 4.5 L1 8" fill="none" stroke="#555"/></svg>Garden Services</h3>
  <ul><li>Garden Clearances</li><li>Regular maintenance programmes</li><li>Hedge cutting</li><li>Flagging, Paving, Decking and Fencing</li><li>Artificial Grass Installation</li><li>Irrigation system installation</li><li>Landscaping Design</li></ul>
</div>
<div class="abs service" style="left:514px">
  <h3><svg width="6" height="9"><path d="M1 1 L5 4.5 L1 8" fill="none" stroke="#555"/></svg>Lawn Services</h3>
  <ul><li>Turfing</li><li>Weed, Pest and Moss control</li><li>Fertiliser applications</li><li>Aeration</li><li>Scarification</li><li>Top Dressing</li><li>Flexible renovation programmes</li></ul>
</div>
<div class="abs service" style="left:705px">
  <h3><svg width="6" height="9"><path d="M1 1 L5 4.5 L1 8" fill="none" stroke="#555"/></svg>Sports Surface Services</h3>
  <ul><li>Turfing</li><li>Weed, Pest and Moss control</li><li>Fertiliser applications</li><li>Aeration</li><li>Scarification</li><li>Top Dressing</li><li>Flexible renovation programmes</li></ul>
</div>

<div class="abs about-band"></div>
<h2 class="abs sec-title" style="left:104px;font-weight:400">Fairway Lawn Care</h2>
<div class="abs subtitle">Tree Garden &amp; Lawn Services</div>
<div class="abs about-img" role="img" aria-label="Lawn mower cutting grass"></div>
<p class="abs about-text">As the name suggests all work is carried out by fully qualified Fairway keepers so why do it yourself?<br>&nbsp;As Fairway keepers the meticulous attention to detail and passion that goes into working on a golf course also goes into every job from general mowing to full hard landscaping jobs and everything in between.<br>Everybody knows that golf greens are the most immaculate, well maintained and most aesthetically pleasing grassed areas on the planet. With this in mind who else would you want to have maintaining .</p>

<h2 class="abs sec-title" style="left:621px;font-weight:400">Testimonials</h2>
<div class="abs quote-img" role="img" aria-label="Portrait of a customer"></div>
<p class="abs quote"><b>&ldquo;</b>Lorem Ipsum is simply dummy text of the printing and typesetting industry. Lorem Ipsum has been the industry's standard dummy text ever since the 1500s, when an unknown printer took a galley of type and scrambled it to make a type specimen book. It has survived not only five centuries, but also the leap into electronic typesetting, remaining essentially unchanged. <b>&rdquo;</b></p>

<section class="abs signup">
  <h2>Sign up for weekly updates</h2>
  <div class="field">Enter Your E-mail address</div>
  <div class="submit">SUBMIT</div>
</section>

<footer class="abs footer"></footer>
<div class="abs social"><span style="background:#d9342b"></span><span style="background:#2a9fd6"></span><span style="background:#3b5998"></span></div>
<div class="abs foot-links">Home<span>|</span>Contact Us<span>|</span>Our Services<span>|</span>Useful Links<span>|</span>Lawncare&nbsp; Advice<span>|</span>FAQS</div>
<div class="abs copy">Copyright ©2013 Fairway lawn Care &nbsp;- All rights reserved</div>
</body>
</html>
```